need corporate, modern business card created for Consulting Company

I need a slick business card using elements from my website, as well as, integrating my pixelharbor-created logo (see files).

The business card needs to be:
1. Corporate and modern
2. Clean and professional

I've included a PSD with the logo/icon that you can use to create it. Feel free to try a metallic finish on the logo, make it bigger/small, underlay it. Whatever you need to do to make my card stand out.

Try a black background, or white background or gray.

The idea is for my card to be memorable as well as professional and corporate.

Target Market(s)

Corporate business in the US and Canada.

Industry/Entity Type

Business

Contact Information for Business Card

Business Leveraging Technology
Malcolm Tudd, Senior Partner
office: 1 877 555 0143
mobile: 1 519 555 0172
website: http://www.vextorial.com

Requirements
Must have
• Card-related information
• corporate, yet modern
• clean and professional
• incorporate the icon only
• must have an editable form when complete!
Nice to have
• metallic icon might be cool
• try it with white or black

```html
<!DOCTYPE html>
<html lang="en">
<head>
<meta charset="utf-8">
<title>Vextorial business card</title>
<link rel="stylesheet" href="https://fonts.googleapis.com/css2?family=Saira:wght@400;500;600&display=swap">
<style>
  :root {
    --page: #ecebe8;
    --ink: #1f1f20;
    --blue: #2f68b5;
    --silver: #b9bbbf;
    --white: #ffffff;
    --card-w: 560px;
    --card-h: 320px;
  }
  * { margin: 0; padding: 0; box-sizing: border-box; }
  html, body { width: 1200px; height: 899px; overflow: hidden; }
  body {
    background: var(--page);
    font-family: "Saira", "Arial", sans-serif;
    position: relative;
  }
  .card {
    position: absolute;
    width: var(--card-w);
    height: var(--card-h);
    overflow: hidden;
    box-shadow: 0 6px 18px rgba(0,0,0,0.18);
  }
  .card-back { left: 170px; top: 95px; }
  .card-front { left: 470px; top: 480px; }
  .card-shapes { position: absolute; inset: 0; width: 100%; height: 100%; }
  .shape-ink { fill: var(--ink); }
  .shape-blue { fill: var(--blue); }
  .shape-silver { fill: var(--silver); }

  .wordmark {
    position: absolute;
    display: flex;
    align-items: center;
    gap: 10px;
    color: var(--blue);
    font-weight: 600;
    font-size: 40px;
    letter-spacing: 0.5px;
    line-height: 1;
  }
  .wordmark-square { width: 18px; height: 18px; background: var(--blue); }
  .card-back .wordmark { left: 330px; top: 120px; }
  .card-front .wordmark { left: 60px; top: 135px; }

  .back-url {
    position: absolute;
    left: 34px;
    top: 180px;
    color: var(--white);
    font-size: 13px;
    font-weight: 500;
    letter-spacing: 0.3px;
  }

  .contact {
    position: absolute;
    right: 28px;
    top: 30px;
    text-align: right;
    color: var(--white);
  }
  .contact-name { font-size: 19px; font-weight: 500; letter-spacing: 1px; text-transform: uppercase; line-height: 1.1; }
  .contact-title { font-size: 13px; margin-top: 2px; }
  .contact-address { font-size: 13px; line-height: 1.35; margin-top: 30px; }
  .contact-lines { list-style: none; margin-top: 28px; font-size: 12px; line-height: 1.95; }
  .contact-lines li { display: flex; justify-content: flex-end; align-items: center; gap: 8px; }
  .contact-lines svg { width: 13px; height: 13px; fill: none; stroke: var(--white); stroke-width: 1.6; stroke-linecap: round; stroke-linejoin: round; }
</style>
</head>
<body>

<section class="card card-back" aria-label="Card back">
  <svg class="card-shapes" viewBox="0 0 560 320" preserveAspectRatio="none" aria-hidden="true">
    <rect class="shape-ink" width="560" height="320"/>
    <polygon class="shape-silver" points="125,0 150,0 232,130 185,320 168,320 212,140"/>
    <polygon class="shape-blue" points="0,0 125,0 212,140 168,320 0,320"/>
  </svg>
  <div class="wordmark"><span class="wordmark-square"></span>vextorial</div>
  <p class="back-url">www.vextorial.com</p>
</section>

<section class="card card-front" aria-label="Card front">
  <svg class="card-shapes" viewBox="0 0 560 320" preserveAspectRatio="none" aria-hidden="true">
    <rect class="shape-blue" width="560" height="320"/>
    <polygon class="shape-silver" points="205,0 222,0 348,145 300,320 290,320 328,148"/>
    <polygon class="shape-ink" points="0,0 205,0 328,148 290,320 0,320"/>
  </svg>
  <div class="wordmark"><span class="wordmark-square"></span>vextorial</div>

  <div class="contact">
    <p class="contact-name">Malcolm Tudd</p>
    <p class="contact-title">Senior Partner</p>
    <p class="contact-address">204, 9th floor, Quay Tower<br>Harbour Road RVT</p>
    <ul class="contact-lines">
      <li>1 877 555 0143
        <svg viewBox="0 0 16 16"><path d="M4 2l2 3-1.5 1.5a8 8 0 0 0 5 5L11 10l3 2-1 2.5C8 14 2 8 1.5 3z"/></svg></li>
      <li>1 519 555 0172
        <svg viewBox="0 0 16 16"><rect x="4.5" y="1.5" width="7" height="13" rx="1.2"/><path d="M7 12.5h2"/></svg></li>
      <li>1 877 555 0168
        <svg viewBox="0 0 16 16"><rect x="2" y="6" width="12" height="8" rx="1"/><path d="M5 6V2h6v4M5 10h6"/></svg></li>
      <li>mtudd@vextorial.com
        <svg viewBox="0 0 16 16"><rect x="1.5" y="3.5" width="13" height="9" rx="1"/><path d="M2 4l6 5 6-5"/></svg></li>
      <li>www.vextorial.com
        <svg viewBox="0 0 16 16"><circle cx="8" cy="8" r="6.5"/><path d="M1.5 8h13M8 1.5c-3 3.5-3 9.5 0 13M8 1.5c3 3.5 3 9.5 0 13"/></svg></li>
    </ul>
  </div>
</section>

</body>
</html>
```